High End Notary Service Business Card Design

Want a professional and elegant/luxurious business card that is clean and simple in the design. A notary is a trusted professional that helps people sign very important documents. The card should be in alignment with this service provided.

Most of the time, service will be for the purchase of a home or refinance of a mortgage

There is NO LOGO. This is aesthetic. A look and feel. Conveying professionalism and concierge level of service.

Target Market(s)

Other business professionals, Lawyers, Escrow Officers, Loan Officers

Industry/Entity Type

Legal

Contact Information for Business Card

This will be a one-sided business card

Colors
35a7d7
3176b5
85cae6
d3a5cc
b868aa
ffffff
0356a4

Requirements
Must have
• Lorena T. Mirabel-Hodgkins
Notary Public

642-871-3094
MirabelSigningDesk@Wexmail.com
Nice to have
• Headshot photo below. Convey the aspect of signing documents. No black cards. Preference is shades of blue: light blue, navy, aqua, gold, white, or lavendar, etc.
Should not have
• No scales or legal scales.

```html
<!DOCTYPE html>
<html lang="en">
<head>
<meta charset="utf-8">
<title>Lorena T. Mirabel-Hodgkins — Notary Public</title>
<link rel="stylesheet" href="https://fonts.googleapis.com/css2?family=Cinzel:wght@700&family=Open+Sans:wght@400&display=swap">
<style>
  :root {
    --page-bg: #f0f0f0;
    --card-blue: #1c5fab;
    --gold: #f6c42b;
    --gold-deep: #d6a737;
    --white: #ffffff;
    --photo-top: #9c9fae;
    --photo-bottom: #b3b5c0;
  }
  html, body {
    margin: 0;
    padding: 0;
    width: 1200px;
    height: 1018px;
    overflow: hidden;
    background: var(--page-bg);
  }
  .business-card {
    position: absolute;
    left: 70px;
    top: 206px;
    width: 1060px;
    height: 606px;
    background: var(--card-blue);
    overflow: hidden;
  }
  .card-artwork {
    position: absolute;
    inset: 0;
    width: 100%;
    height: 100%;
  }
  .identity {
    position: absolute;
    left: 573px;
    top: 120px;
    width: 400px;
    text-align: center;
    font-family: "Cinzel", Georgia, serif;
    font-weight: 700;
  }
  .identity__name {
    margin: 0;
    color: var(--white);
    font-size: 26px;
    line-height: 32px;
    white-space: nowrap;
  }
  .identity__rule {
    display: block;
    width: 382px;
    height: 2px;
    margin: 4px auto 2px;
    background: var(--gold);
  }
  .identity__title {
    margin: 0;
    color: var(--gold);
    font-size: 27px;
    line-height: 32px;
  }
  .contact-list {
    position: absolute;
    left: 573px;
    top: 446px;
    margin: 0;
    padding: 0;
    list-style: none;
    font-family: "Open Sans", Arial, sans-serif;
    color: var(--white);
    font-size: 24px;
  }
  .contact-list__item {
    display: flex;
    align-items: center;
    gap: 6px;
    height: 42px;
    margin-bottom: 8px;
  }
  .contact-list__icon {
    width: 40px;
    height: 40px;
    flex: none;
  }
</style>
</head>
<body>
  <div class="business-card">
    <svg class="card-artwork" viewBox="0 0 1642 938" preserveAspectRatio="none">
      <defs>
        <linearGradient id="portrait-tone" x1="0" y1="0" x2="0" y2="1">
          <stop offset="0" stop-color="var(--photo-top)"/>
          <stop offset="1" stop-color="var(--photo-bottom)"/>
        </linearGradient>
      </defs>
      <path class="gold-arc" fill="var(--gold)"
        d="M662,0 L672,0 C790,150 860,300 850,435 C845,650 760,820 680,938 L527,938 C680,780 800,600 789,400 C780,250 720,100 662,0 Z"/>
      <path class="gold-arc-shade" fill="var(--gold-deep)"
        d="M848,500 C835,700 760,830 680,938 L585,938 C710,820 810,680 848,500 Z"/>
      <path class="portrait-area" role="img" aria-label="Headshot portrait of the notary against a soft grey backdrop"
        fill="url(#portrait-tone)"
        d="M0,0 L662,0 C720,100 780,250 789,400 C800,600 680,780 527,938 L0,938 Z"/>
    </svg>

    <div class="identity">
      <h1 class="identity__name">Lorena T. Mirabel-Hodgkins</h1>
      <span class="identity__rule"></span>
      <p class="identity__title">Notary Public</p>
    </div>

    <ul class="contact-list">
      <li class="contact-list__item">
        <svg class="contact-list__icon" viewBox="0 0 40 40" aria-hidden="true">
          <circle cx="20" cy="20" r="20" fill="var(--gold)"/>
          <path fill="var(--card-blue)" d="M14.5,10.5 l3.5,-1 l2.5,6 l-2.5,1.8 c0.8,3 2.5,5.5 5,7 l2.3,-2 l5,3.8 l-1.5,3.2 c-1.5,1.4 -4,1.5 -6.5,0 c-5,-3 -8.5,-8.5 -9.3,-13.6 c-0.3,-2.3 0.7,-4.2 1.5,-5.2 Z"/>
        </svg>
        <span class="contact-list__text">642-871-3094</span>
      </li>
      <li class="contact-list__item">
        <svg class="contact-list__icon" viewBox="0 0 40 40" aria-hidden="true">
          <circle cx="20" cy="20" r="20" fill="var(--gold)"/>
          <rect x="10" y="13" width="20" height="14" fill="none" stroke="var(--card-blue)" stroke-width="2.4"/>
          <path d="M10.5,14 L20,21.5 L29.5,14" fill="none" stroke="var(--card-blue)" stroke-width="2.4"/>
        </svg>
        <span class="contact-list__text">MirabelSigningDesk@Wexmail.com</span>
      </li>
    </ul>
  </div>
</body>
</html>
```